Design for Dex Halloran's Grizzle Rinse

Dex Halloran will be launching our new body wash April 1st and are looking for a beastly beast to put on our label for the body wash.
We will make the rest of the label but we want someone to design a good beast to put on the front of the bottle.
We want him to be moving left and at a 45-degree angle.

Target Market(s)

18-34 Males

Industry/Entity Type

Hair Care Product

Colors
000000
ffffff
5c5c5c
aaaaaa
dbdbdb

Requirements
Must have
• A beast looking creature.
• Black and white/grey
• Realism but not too much detail. It will be shrunk down to 1 inch by 1 inch
Should not have
• No colors or cartoon styles
• No profile images or

```html
<!DOCTYPE html>
<html lang="en">
<head>
<meta charset="utf-8">
<title>Dex Halloran's Grizzle Rinse — Label</title>
<link rel="stylesheet" href="https://fonts.googleapis.com/css2?family=Questrial&family=Open+Sans:wght@400;700&display=swap">
<style>
  :root {
    --black: #000000;
    --label: #050505;
    --white: #ffffff;
    --grey-dark: #5c5c5c;
    --grey-mid: #aaaaaa;
    --grey-light: #dbdbdb;
    --page: #ffffff;
  }
  html, body {
    margin: 0;
    padding: 0;
    width: 1200px;
    height: 848px;
    overflow: hidden;
    background: var(--page);
  }
  .label {
    position: absolute;
    left: 55px;
    top: 24px;
    width: 1090px;
    height: 801px;
    background: var(--label);
    overflow: hidden;
  }
  .beast-frame {
    position: absolute;
    left: 48px;
    top: 168px;
    width: 404px;
    height: 388px;
    border: 1.5px solid var(--grey-mid);
    border-radius: 24px;
    box-sizing: border-box;
    overflow: hidden;
  }
  .beast-frame svg { display: block; width: 100%; height: 100%; }
  .brand-owner {
    position: absolute;
    left: 474px;
    top: 160px;
    margin: 0;
    font-family: "Questrial", sans-serif;
    font-weight: 400;
    font-size: 74px;
    line-height: 1;
    color: var(--grey-mid);
    letter-spacing: 1px;
    white-space: nowrap;
  }
  .product-name {
    position: absolute;
    left: 474px;
    top: 244px;
    margin: 0;
    font-family: "Questrial", sans-serif;
    font-weight: 400;
    font-size: 84px;
    line-height: 1;
    color: var(--white);
    white-space: nowrap;
  }
  .product-type {
    position: absolute;
    left: 480px;
    top: 352px;
    margin: 0;
    font-family: "Open Sans", sans-serif;
    font-weight: 700;
    font-size: 21px;
    letter-spacing: 4.2px;
    color: var(--white);
    white-space: nowrap;
  }
  .description {
    position: absolute;
    left: 480px;
    top: 384px;
    width: 561px;
    margin: 0;
    font-family: "Open Sans", sans-serif;
    font-size: 17px;
    line-height: 23.5px;
    color: var(--white);
    text-align: justify;
  }
  .volume {
    position: absolute;
    left: 819px;
    top: 705px;
    width: 156px;
    height: 120px;
    border: 1.5px solid var(--grey-mid);
    border-bottom: none;
    box-sizing: border-box;
    font-family: "Open Sans", sans-serif;
    font-weight: 700;
    font-size: 30px;
    letter-spacing: 5px;
    color: var(--white);
    text-align: center;
    padding-top: 20px;
  }
</style>
</head>
<body>
  <section class="label">
    <div class="beast-frame">
      <svg role="img" aria-label="Grey silhouette illustration of a hulking beast striding left at an angle" viewBox="0 0 404 388" preserveAspectRatio="none">
        <defs>
          <radialGradient id="beast-tone" cx="50%" cy="45%" r="60%">
            <stop offset="0%" stop-color="#8a8a8a"/>
            <stop offset="100%" stop-color="#050505"/>
          </radialGradient>
        </defs>
        <rect width="404" height="388" fill="url(#beast-tone)"/>
      </svg>
    </div>
    <h1 class="brand-owner">Dex Halloran's</h1>
    <h2 class="product-name">Grizzle Rinse</h2>
    <p class="product-type">HYDRATING HAND AND BODY LOTION</p>
    <p class="description">Try the new dex halloran grizzle rinse, crafted with 98 percent pure glycerin and natural oils. It is a pure and gentle cleanser for your body that leaves your skin feeling soft, smooth and moisturised. dex halloran grizzle rinse is mild and gentle and cleanses your skin thoroughly. It is 100 percent soap free and dermatologically tested. It helps moisturise your skin so that it does not dry. With natural oils, it is a gentle cleanser for your body.</p>
    <div class="volume">190mL</div>
  </section>
</body>
</html>
```